TR Stationery - Modern Contemporary

Develop modern template for Letterhead and Stationery (business card, letterhead, envelopes) using the TR Logo and Icon

Colors
0054AA
0677BA
7BADD7
CADEEF
E8F1F8
00AB8E
00BBA5
67D7C9
C6EFE9
E9F9F6
EE7325
F08F49
F5BC92
FAE3D3
FDF4ED
6B429C
8869AF
B7A5CE
E3DAEB
F3F0F8

```html
<!DOCTYPE html>
<html lang="en">
<head>
<meta charset="utf-8">
<title>TR Stationery</title>
<link href="https://fonts.googleapis.com/css2?family=Arimo:wght@400;700&display=swap" rel="stylesheet">
<style>
:root{
  --bg:#a9a7a8;
  --navy:#2b304a;
  --navy-deep:#222639;
  --paper:#f8f8f8;
  --white:#ffffff;
  --green:#2fb36a;
  --orange:#ee7325;
  --ink:#2b304a;
  --grey-text:#4a4d5c;
  --rule:#2b304a;
}
*{margin:0;padding:0;box-sizing:border-box}
html,body{width:828px;height:1200px;overflow:hidden;background:var(--bg)}
body{position:relative;font-family:'Arimo',Arial,sans-serif;color:var(--ink)}
.piece{position:absolute;overflow:hidden;box-shadow:2px 3px 5px rgba(0,0,0,.25)}
.wordmark{font-family:'Arimo',Arial,sans-serif;font-weight:400;letter-spacing:.02em;white-space:nowrap;line-height:1}
.wordmark.on-light{color:var(--navy)}
.wordmark.on-dark{color:var(--white)}
.wordmark.embossed{color:var(--navy-deep);text-shadow:0 1px 0 rgba(255,255,255,.08)}
.footer-band{position:absolute;left:0;bottom:0;width:100%}
.footer-url{position:absolute;left:0;bottom:0;color:var(--white);font-weight:700}
.icon{display:inline-block;vertical-align:middle;margin-right:5px}

/* business card front */
.card-front{left:57px;top:58px;width:305px;height:174px;background:var(--paper)}
.card-front .wordmark{position:absolute;left:17px;top:22px;font-size:21px}
.card-name{position:absolute;left:17px;top:92px;font-size:10.5px;font-weight:700;color:var(--green);letter-spacing:.02em}
.card-role{position:absolute;left:17px;top:106px;font-size:8.5px;color:var(--grey-text)}
.card-rule{position:absolute;left:17px;top:118px;width:270px;height:1px;background:var(--rule)}
.card-contact{position:absolute;left:19px;top:127px;font-size:8px;line-height:11px;color:var(--grey-text)}
.card-address{position:absolute;right:18px;top:127px;font-size:8px;line-height:11px;text-align:right;color:var(--grey-text)}
.card-front .footer-url{font-size:7.5px;left:19px;bottom:4px}

.card-back{left:57px;top:254px;width:305px;height:174px;background:var(--navy);display:flex;align-items:center;justify-content:center}
.card-back .wordmark{font-size:24px}
.card-emboss{left:57px;top:457px;width:305px;height:174px;background:var(--navy);display:flex;align-items:center;justify-content:center}
.card-emboss .wordmark{font-size:24px}

/* envelopes */
.envelope-front{left:390px;top:66px;width:395px;height:172px;background:var(--paper)}
.envelope-front .wordmark{position:absolute;left:13px;top:13px;font-size:11px}
.envelope-return{position:absolute;left:13px;top:25px;font-size:4.5px;line-height:5px;color:var(--grey-text)}
.envelope-front .footer-url{font-size:7.5px;left:13px;bottom:5px}

.envelope-back{left:390px;top:262px;width:395px;height:172px;background:var(--paper)}
.envelope-back.dark-flap{top:459px;background:var(--white)}
.flap{position:absolute;left:0;top:0;width:395px;height:50px}
.flap .wordmark{position:absolute;left:0;right:0;top:14px;text-align:center;font-size:16px}

/* letterhead */
.letterhead{left:50px;top:660px;width:360px;height:509px;background:var(--paper)}
.lh-header{position:absolute;left:32px;top:29px;width:296px;height:24px;border-bottom:1px solid var(--rule);display:flex;align-items:flex-start}
.lh-header .wordmark{font-size:17px;margin-top:1px}
.lh-divider{width:1px;height:15px;background:var(--rule);margin:1px 14px 0}
.lh-detail{font-size:5.8px;line-height:7.4px;color:var(--grey-text)}
.lh-salute{position:absolute;left:33px;top:157px;font-size:8px;font-weight:700;color:var(--grey-text)}
.lh-body{position:absolute;left:32px;top:180px;width:297px;font-size:5.9px;line-height:7.4px;color:var(--grey-text)}
.lh-body p{margin-bottom:6px}
.lh-close{position:absolute;left:33px;top:333px;font-size:4.8px;font-weight:700;color:var(--grey-text)}
.signature-area{position:absolute;left:32px;top:348px;width:60px;height:18px;background:linear-gradient(90deg,#e4e4e6,#eeeeef);border-radius:3px}
.letterhead .footer-url{font-size:7.5px;left:32px;bottom:5px}

/* folders */
.folder-closed{left:435px;top:660px;width:342px;height:241px;background:var(--paper)}
.folder-cover{position:absolute;left:0;top:0;width:171px;height:241px;background:var(--navy);display:flex;align-items:center;justify-content:center}
.folder-cover .wordmark{font-size:15px}
.insert{position:absolute;background:linear-gradient(90deg,#ffffff 0%,#f2f2f2 60%,#e9e9e9 100%)}
.insert-closed{left:171px;top:0;width:171px;height:241px}
.mini-header{position:absolute;display:flex;align-items:flex-start;border-bottom:.6px solid var(--rule)}
.mini-divider{width:.6px;background:var(--rule)}
.mini-detail{color:var(--grey-text)}
.mini-text{position:absolute;color:var(--grey-text)}
.mini-text p{margin-bottom:2.4px}
.insert-closed .mini-header{left:15px;top:14px;width:142px;height:9px}
.insert-closed .wordmark{font-size:8px}
.insert-closed .mini-divider{height:6px;margin:1px 6px 0}
.insert-closed .mini-detail{font-size:2.2px;line-height:2.8px}
.insert-closed .mini-salute{position:absolute;left:15px;top:75px;font-size:3.4px;font-weight:700;color:var(--grey-text)}
.insert-closed .mini-text{left:15px;top:85px;width:140px;font-size:2.3px;line-height:3px}
.insert-closed .signature-area{left:15px;top:167px;width:26px;height:7px}
.insert-closed .footer-url{font-size:3.2px;left:15px;bottom:2px}

.folder-open{left:435px;top:927px;width:342px;height:242px;background:var(--white)}
.inner-panel{position:absolute;left:0;top:0;width:171px;height:242px;background:linear-gradient(90deg,#ffffff 0%,#f3f3f3 70%,#dcdcdc 100%)}
.inner-panel.right{left:171px;background:linear-gradient(90deg,#ececec 0%,#f7f7f7 30%,#ffffff 100%)}
.insert-open{left:179px;top:8px;width:152px;height:146px;background:#fafafa;box-shadow:0 0 3px rgba(0,0,0,.1)}
.insert-open .mini-header{left:14px;top:14px;width:126px;height:8px}
.insert-open .wordmark{font-size:7.5px}
.insert-open .mini-divider{height:5px;margin:1px 6px 0}
.insert-open .mini-detail{font-size:2px;line-height:2.5px}
.insert-open .mini-salute{position:absolute;left:14px;top:75px;font-size:3px;font-weight:700;color:var(--grey-text)}
.insert-open .mini-text{left:14px;top:84px;width:125px;font-size:2.1px;line-height:2.7px}
.pockets{position:absolute;left:0;top:153px;width:342px;height:89px}
</style>
</head>
<body>

<!-- business card front -->
<section class="piece card-front" aria-label="Business card front">
  <div class="wordmark on-light">terra ridge</div>
  <div class="card-name">DANIEL REYES</div>
  <div class="card-role">Manager</div>
  <div class="card-rule"></div>
  <div class="card-contact">
    <div><svg class="icon" width="7" height="7" viewBox="0 0 10 10"><path d="M2 1l2 2-1 1.5c.8 1.4 1.6 2.2 3 3L7.5 6l2 2-1.5 1.5C4.5 9 1 5.5.5 2.5z" fill="var(--green)"/></svg>555-014-2100</div>
    <div><svg class="icon" width="7" height="7" viewBox="0 0 10 10"><rect x=".8" y="2" width="8.4" height="6" fill="none" stroke="var(--green)" stroke-width="1"/><path d="M1 2.3l4 3 4-3" fill="none" stroke="var(--green)" stroke-width="1"/></svg>info@terraridge.com</div>
  </div>
  <div class="card-address">Your address, city<br>state, ZIP 0000</div>
  <svg class="footer-band" width="305" height="17" viewBox="0 0 305 17" preserveAspectRatio="none">
    <path d="M0 3H126C132 3 134 10 142 10H305V17H0Z" fill="var(--navy)"/>
    <rect x="134" y="7" width="96" height="2.2" fill="var(--green)"/>
    <rect x="225" y="7" width="80" height="2.2" fill="var(--orange)"/>
  </svg>
  <div class="footer-url">www.terraridge.com</div>
</section>

<section class="piece card-back" aria-label="Business card back">
  <div class="wordmark on-dark">terra ridge</div>
</section>

<section class="piece card-emboss" aria-label="Business card back, embossed">
  <div class="wordmark embossed">terra ridge</div>
</section>

<!-- envelope front -->
<section class="piece envelope-front" aria-label="Envelope front">
  <div class="wordmark on-light">terra ridge</div>
  <div class="envelope-return">Your address, city<br>state, ZIP 0000</div>
  <svg class="footer-band" width="395" height="17" viewBox="0 0 395 17" preserveAspectRatio="none">
    <path d="M0 2H116C122 2 124 8 132 8H395V17H0Z" fill="var(--navy)"/>
    <rect x="128" y="4.5" width="140" height="2.4" fill="var(--green)"/>
    <rect x="268" y="4.5" width="127" height="2.4" fill="var(--orange)"/>
  </svg>
  <div class="footer-url">www.terraridge.com</div>
</section>

<!-- envelope back, light flap -->
<section class="piece envelope-back" aria-label="Envelope back">
  <svg class="flap" viewBox="0 0 395 50" preserveAspectRatio="none">
    <path d="M0 0H395L386 34Q383 47 369 47H26Q12 47 9 34Z" fill="var(--white)" style="filter:drop-shadow(0 2px 2px rgba(0,0,0,.18))"/>
  </svg>
  <div class="flap"><div class="wordmark on-light">terra ridge</div></div>
</section>

<!-- envelope back, dark flap -->
<section class="piece envelope-back dark-flap" aria-label="Envelope back, dark flap">
  <svg class="flap" viewBox="0 0 395 50" preserveAspectRatio="none">
    <path d="M0 0H395L386 34Q383 47 369 47H26Q12 47 9 34Z" fill="var(--navy)" style="filter:drop-shadow(0 2px 2px rgba(0,0,0,.2))"/>
  </svg>
  <div class="flap"><div class="wordmark on-dark">terra ridge</div></div>
</section>

<!-- letterhead -->
<section class="piece letterhead" aria-label="Letterhead">
  <header class="lh-header">
    <div class="wordmark on-light">terra ridge</div>
    <div class="lh-divider"></div>
    <div class="lh-detail">
      <div><svg class="icon" width="5" height="5" viewBox="0 0 10 10"><path d="M2 1l2 2-1 1.5c.8 1.4 1.6 2.2 3 3L7.5 6l2 2-1.5 1.5C4.5 9 1 5.5.5 2.5z" fill="var(--green)"/></svg>555-014-2100</div>
      <div><svg class="icon" width="5" height="5" viewBox="0 0 10 10"><rect x=".8" y="2" width="8.4" height="6" fill="var(--green)"/></svg>info@terraridge.com</div>
    </div>
    <div class="lh-divider"></div>
    <div class="lh-detail">Your address, city<br>state, ZIP 0000</div>
  </header>
  <div class="lh-salute">Dear Mr. Reyes,</div>
  <div class="lh-body">
    <p>Lorem ipsum dolor sit amet, consectetuer adipiscing elit, sed diam nonummy nibh euismod tincidunt ut laoreet dolore magna aliquam erat volutpat. Ut wisi enim ad minim veniam, quis nostrud exerci tationmcorper suscipit lobortis nisl ut aliquip ex ea commodo consequat. Duis autem vel eum iriure dolor in hendrerit in vulputate velit esse molestie consequat, vel illum dolore eu feugiat</p>
    <p>Rorem ipsum dolor sit amet, consectetuer adipiscing elit, sed diam nonummy nibh euismod tincidunt ut laoreet dolore magna aliquam erat volutpat. Ut wisi enim ad minim veniam, quis nostrud exerci tationmcorper suscipit lobortis nisl ut aliquip ex ea commodo consequat. Duis autem vel eum iriure dolor in hendrerit in vulputate velit esse molest</p>
    <p>Dorem ipsum dolor sit amet, consectetuer adipiscing elit, sed diam nonummy nibh euismod tincidunt ut laoreet dolore magna aliquam erat volutpat. Ut wisi enim ad minim veniam, quis nostrud exerci tationmcorper suscipit lobortis nisl ut aliquip ex ea commodo consequat. Duis autem vel eum iriure dolor in hendrerit in suscipit lobortis nisl ut aliquip ex ea commodo consequat. Duis autem vel eum iriure dolor in hendrerit in vulputate velit esse molestie consequat, vel illum</p>
    <p>Sorem ipsum dolor sit amet, consectetuer adipiscing elit, sed diam nonummy nibh euismod tincidunt ut laoreet dolore magna aliquam erat volutpat. Ut wisi enim ad minim veniam, quis nostrud exerci tationmcorper suscipit lobortis nisl ut aliquip ex ea commodo consequat. Duis autem vel eum iriure dolor in</p>
  </div>
  <div class="lh-close">Sincerely,</div>
  <div class="signature-area" role="img" aria-label="Handwritten signature"></div>
  <svg class="footer-band" width="360" height="17" viewBox="0 0 360 17" preserveAspectRatio="none">
    <path d="M0 2H128C134 2 136 8 144 8H360V17H0Z" fill="var(--navy)"/>
    <rect x="134" y="5" width="107" height="2.4" fill="var(--green)"/>
    <rect x="241" y="5" width="119" height="2.4" fill="var(--orange)"/>
  </svg>
  <div class="footer-url">www.terraridge.com</div>
</section>

<!-- presentation folder, closed -->
<section class="piece folder-closed" aria-label="Presentation folder cover with letter">
  <div class="folder-cover"><div class="wordmark on-dark">terra ridge</div></div>
  <div class="insert insert-closed">
    <div class="mini-header">
      <div class="wordmark on-light">terra ridge</div>
      <div class="mini-divider"></div>
      <div class="mini-detail">555-014-2100<br>info@terraridge.com</div>
      <div class="mini-divider"></div>
      <div class="mini-detail">Your address, city<br>state, ZIP 0000</div>
    </div>
    <div class="mini-salute">Dear Mr. Reyes,</div>
    <div class="mini-text">
      <p>Lorem ipsum dolor sit amet, consectetuer adipiscing elit, sed diam nonummy nibh euismod tincidunt. Lorem ipsum dolor sit amet, consectetuer adipiscing elit, sed diam nonummy nibh euismod tincidunt.</p>
      <p>Lorem ipsum dolor sit amet, consectetuer adipiscing elit, sed diam nonummy nibh euismod tincidunt. Lorem ipsum dolor sit amet, consectetuer adipiscing elit, sed diam nonummy nibh euismod tincidunt.</p>
      <p>Lorem ipsum dolor sit amet, consectetuer adipiscing elit, sed diam nonummy nibh euismod tincidunt. Lorem ipsum dolor sit amet, consectetuer adipiscing elit, sed diam nonummy nibh euismod tincidunt.</p>
      <p>Lorem ipsum dolor sit amet, consectetuer adipiscing elit, sed diam nonummy nibh euismod tincidunt. Lorem ipsum dolor sit amet, consectetuer adipiscing elit, sed diam nonummy nibh euismod tincidunt.</p>
    </div>
    <div class="signature-area" role="img" aria-label="Handwritten signature"></div>
    <svg class="footer-band" width="171" height="8" viewBox="0 0 171 8" preserveAspectRatio="none">
      <path d="M0 1H58C61 1 62 4 66 4H171V8H0Z" fill="var(--navy)"/>
      <rect x="62" y="2.4" width="52" height="1.2" fill="var(--green)"/>
      <rect x="114" y="2.4" width="57" height="1.2" fill="var(--orange)"/>
    </svg>
    <div class="footer-url">www.terraridge.com</div>
  </div>
</section>

<!-- presentation folder, open -->
<section class="piece folder-open" aria-label="Presentation folder inside with letter">
  <div class="inner-panel"></div>
  <div class="inner-panel right"></div>
  <div class="insert insert-open">
    <div class="mini-header">
      <div class="wordmark on-light">terra ridge</div>
      <div class="mini-divider"></div>
      <div class="mini-detail">555-014-2100<br>info@terraridge.com</div>
      <div class="mini-divider"></div>
      <div class="mini-detail">Your address, city<br>state, ZIP 0000</div>
    </div>
    <div class="mini-salute">Dear Mr. Reyes,</div>
    <div class="mini-text">
      <p>Lorem ipsum dolor sit amet, consectetuer adipiscing elit, sed diam nonummy nibh euismod tincidunt. Lorem ipsum dolor sit amet, consectetuer adipiscing elit, sed diam nonummy nibh euismod tincidunt.</p>
      <p>Lorem ipsum dolor sit amet, consectetuer adipiscing elit, sed diam nonummy nibh euismod tincidunt. Lorem ipsum dolor sit amet, consectetuer adipiscing elit, sed diam nonummy nibh euismod tincidunt.</p>
      <p>Lorem ipsum dolor sit amet, consectetuer adipiscing elit, sed diam nonummy nibh euismod tincidunt. Lorem ipsum dolor sit amet, consectetuer adipiscing elit, sed diam nonummy nibh euismod tincidunt.</p>
      <p>Lorem ipsum dolor sit amet, consectetuer adipiscing elit, sed diam nonummy nibh euismod tincidunt. Lorem ipsum dolor sit amet, consectetuer adipiscing elit, sed diam nonummy nibh euismod tincidunt.</p>
    </div>
  </div>
  <svg class="pockets" viewBox="0 0 342 89" preserveAspectRatio="none">
    <path d="M0 0H158Q164 0 164 8L171 89H0Z" fill="var(--navy)"/>
    <path d="M342 0H184Q178 0 177 8L171 89H342Z" fill="var(--navy)"/>
  </svg>
</section>

</body>
</html>
```